Book on a defense of Christianity needs a cover design.

I need a cover for a book providing a fair and balanced factually supported logical defense of three sources related to Christian beliefs: Elder Codex, Latter Codex, and Scroll of Keravin. It is written in easy to follow language in a father-to-son question and answer format. There are extensive footnotes that allow the reader to go to the source and research all things stated in the book. Both the positive evidence and the negative evidence is presented in respectful language. The final point is a proof of the validity of Christian basic beliefs. The title of the book is: Listen Closely, Child: Where Belief Meets Doubt. Letters from a father to his son regarding an evidence based logical approach to combat the secular attacks on Christianity.
Target Market(s)
General public
Industry/Entity Type
Defense
Requirements
Nice to have
- Color. Attention grabbing design. Can be abstract.

```html
<!DOCTYPE html>
<html lang="en">
<head>
<meta charset="utf-8">
<title>Listen Closely, Child: Where Belief Meets Doubt — Cover</title>
<link rel="stylesheet" href="https://fonts.googleapis.com/css2?family=Tinos&family=Great+Vibes&family=Yanone+Kaffeesatz:wght@400&display=swap">
<style>
  :root {
    --ink: #000000;
    --light: #ffffff;
    --glow-edge: rgba(255,255,255,0);
  }
  * { margin: 0; padding: 0; box-sizing: border-box; }
  html, body { width: 857px; height: 1200px; overflow: hidden; background: var(--ink); }
  .cover {
    position: relative;
    width: 857px;
    height: 1200px;
    background: var(--ink);
    overflow: hidden;
    isolation: isolate;
  }
  .light-band {
    position: absolute;
    top: 0;
    left: 347px;
    width: 176px;
    height: 100%;
    background: linear-gradient(to right,
      var(--glow-edge) 0%,
      rgba(255,255,255,0.55) 12%,
      var(--light) 32%,
      var(--light) 62%,
      rgba(255,255,255,0.5) 85%,
      var(--glow-edge) 100%);
  }
  .cover-text {
    position: absolute;
    left: 0;
    width: 100%;
    text-align: center;
    color: var(--light);
    mix-blend-mode: difference;
    white-space: nowrap;
  }
  .tagline {
    top: 180px;
    font-family: "Tinos", "Times New Roman", serif;
    font-size: 62px;
    letter-spacing: -0.5px;
  }
  .tagline .key-word { margin: 0 16px; }
  .title {
    top: 530px;
    display: flex;
    justify-content: center;
    align-items: baseline;
    gap: 18px;
    line-height: 1;
    font-weight: 400;
  }
  .title .opening {
    font-family: "Great Vibes", cursive;
    font-size: 104px;
  }
  .title .rest {
    display: inline-block;
    font-family: "Yanone Kaffeesatz", sans-serif;
    font-size: 90px;
    transform: skewX(-10deg) scaleY(1.3);
    transform-origin: left bottom;
    word-spacing: 6px;
  }
  .subtitle {
    top: 760px;
    font-family: "Tinos", "Times New Roman", serif;
    font-size: 42px;
    letter-spacing: -0.5px;
  }
</style>
</head>
<body>
  <main class="cover">
    <div class="light-band"></div>
    <p class="cover-text tagline">Where your<span class="key-word">belief</span>meets doubt</p>
    <h1 class="cover-text title"><span class="opening">“Listen</span><span class="rest">closely, child....”</span></h1>
    <p class="cover-text subtitle">Letters from a father</p>
  </main>
</body>
</html>
```